LUSTRIA INC. is a new Fashion Stylist, Design Merchandiser, and consultant in the fashion industry

We need a logo design for a new Calgary, Alberta based company that is in the business of making over your image, wardrobe and style for both business and personal purposes.

Target Market(s)

Professional female and male business people looking for a new style or complete fashion makeover including clothes closet merchandising and makeover.

Contact Information for Business Card

Number of Pages Required

1 page

Font styles to use
Script

Colors
fac994
fbe7d2
fee3d4

Requirements
Must have
• Fashion Industry theme that is very elegant and colorful using gold/bronze/silver color themes.
Nice to have
• Incorporate the company name with the creative font to come up with the appropriate "logo"

```html
<!DOCTYPE html>
<html lang="en">
<head>
<meta charset="utf-8">
<title>Lustria Inc. — Business Card</title>
<link rel="stylesheet" href="https://fonts.googleapis.com/css2?family=Damion&family=Roboto:wght@400;700&display=swap">
<style>
  :root {
    --backdrop: #2a2a2b;
    --card: #fbe7d6;
    --gold: #b8912e;
    --ink: #111111;
    --watermark: #efd9c6;
  }
  * { box-sizing: border-box; margin: 0; padding: 0; }
  html, body { width: 1200px; height: 880px; overflow: hidden; }
  body { background: var(--backdrop); position: relative; font-family: "Roboto", sans-serif; }

  .card {
    position: absolute;
    width: 560px;
    height: 320px;
    background: var(--card);
    border-radius: 24px;
    box-shadow: 0 10px 28px rgba(0,0,0,0.45);
    overflow: hidden;
  }
  .card--front { left: 90px; top: 110px; }
  .card--back  { left: 550px; top: 450px; }

  .brand {
    position: absolute;
    left: 0; right: 0; top: 0; bottom: 0;
    display: flex;
    align-items: center;
    justify-content: center;
    gap: 14px;
  }
  .brand__dot {
    width: 22px;
    height: 22px;
    border-radius: 50%;
    background: var(--gold);
  }
  .brand__name {
    font-family: "Roboto", sans-serif;
    font-weight: 700;
    font-size: 34px;
    letter-spacing: 3px;
    line-height: 1;
    color: var(--gold);
  }

  .watermark {
    position: absolute;
    left: 150px; top: 30px;
    width: 260px; height: 260px;
    border-radius: 50%;
    background: var(--watermark);
    opacity: 0.55;
  }

  .contact {
    position: absolute;
    left: 0; right: 0; top: 98px;
    text-align: center;
  }
  .contact__name {
    font-family: "Damion", cursive;
    font-size: 40px;
    line-height: 1.1;
    color: var(--ink);
  }
  .contact__title {
    margin-top: 6px;
    font-size: 16px;
    letter-spacing: 0.5px;
    color: var(--ink);
  }
  .contact__phone {
    margin-top: 22px;
    font-size: 20px;
    font-weight: 700;
    letter-spacing: 1px;
    color: var(--ink);
  }
</style>
</head>
<body>
  <section class="card card--front" aria-label="Card front">
    <div class="brand">
      <span class="brand__dot" aria-hidden="true"></span>
      <span class="brand__name">LUSTRIA INC.</span>
    </div>
  </section>

  <section class="card card--back" aria-label="Card back">
    <div class="watermark" role="img" aria-label="Faint brand decoration in pale peach"></div>
    <div class="contact">
      <div class="contact__name">Maren Holloway</div>
      <div class="contact__title">fashion stylist design merchandiser consultant</div>
      <div class="contact__phone">403-555-0182</div>
    </div>
  </section>
</body>
</html>
```